Invitation Design Project

I need a customized graphic design for my wedding invitation.I want it to be non-traditional wedding invite. The design in mind is like a movie poster graphics while adopting 'the brighter days of the islands' font style and colors that create a light mood at the front page.Inside pages can be similar to movie posters with dark background similar to that of Ashen warden.Wedding related art/graphics can be integrated within the design.Wordings can be discussed later.

Industry/Entity Type

Graphic Design

Requirements
Must have
• Other must have features are our pictures as couple which will be sent .
Nice to have
• we would like to have the words

"our wedding.

more fun if you'll come!"

on the front cover.

```html
<!DOCTYPE html>
<html lang="en">
<head>
<meta charset="utf-8">
<title>Our Wedding – Invitation</title>
<link href="https://fonts.googleapis.com/css2?family=Libre+Baskerville:wght@400;700&family=Cinzel:wght@500;700&family=Poppins:wght@600&family=Nunito:wght@800&display=swap" rel="stylesheet">
<style>
  :root {
    --red: #ec1c2b;
    --black: #000000;
    --white: #ffffff;
    --photo-grey: #bcbdc0;
    --ink: #111111;
  }
  * { margin: 0; padding: 0; box-sizing: border-box; }
  html, body { width: 900px; height: 1200px; overflow: hidden; background: var(--white); }
  .invitation {
    position: relative;
    width: 900px;
    height: 1200px;
    background: var(--white);
    overflow: hidden;
  }
  .bride-bar {
    position: absolute; left: 0; top: 0;
    width: 688px; height: 160px;
    background: var(--red);
  }
  .bride-name {
    position: absolute; left: 62px; top: 48px;
    font: 700 44px/1 "Libre Baskerville", serif;
    color: var(--white);
  }
  .groom-bar {
    position: absolute; left: 212px; top: 162px;
    width: 688px; height: 161px;
    background: var(--black);
  }
  .groom-name {
    position: absolute; right: 72px; top: 58px;
    font: 700 44px/1 "Libre Baskerville", serif;
    color: var(--white);
  }
  .starring {
    position: absolute; left: 0; top: 332px; width: 900px;
    text-align: center;
    font: 400 40px/1 "Libre Baskerville", serif;
    letter-spacing: 9px;
    color: var(--ink);
  }
  .title {
    position: absolute; left: 22px; top: 378px;
    font: 600 128px/1 "Poppins", sans-serif;
    letter-spacing: 1px;
    color: var(--red);
    white-space: nowrap;
  }
  .tagline-band {
    position: absolute; left: 0; top: 517px;
    width: 875px; height: 52px;
    background: var(--black);
  }
  .tagline {
    position: absolute; right: 35px; top: 8px;
    font: 800 33px/1 "Nunito", sans-serif;
    color: var(--white);
    white-space: nowrap;
  }
  .photo-area {
    position: absolute; left: 0; top: 579px;
    width: 900px; height: 621px;
    background: var(--photo-grey);
  }
  .photo-label {
    position: absolute; left: 0; top: 110px; width: 900px;
    text-align: center;
    font: 700 84px/1 "Libre Baskerville", serif;
    color: var(--black);
  }
  .date-block {
    position: absolute; left: 0; top: 1033px;
    width: 688px; height: 167px;
    background: var(--black);
    color: var(--white);
    text-align: center;
  }
  .date-headline {
    margin-top: 22px;
    font: 700 45px/1 "Cinzel", serif;
    letter-spacing: 1px;
  }
  .date-detail {
    font: 700 28px/1.3 "Cinzel", serif;
    letter-spacing: 5px;
  }
  .date-detail:first-of-type { margin-top: 14px; }
</style>
</head>
<body>
  <main class="invitation">
    <div class="bride-bar"><span class="bride-name">brides name</span></div>
    <div class="groom-bar"><span class="groom-name">grooms name</span></div>

    <p class="starring">starring in</p>
    <h1 class="title">Our Wedding</h1>
    <div class="tagline-band"><span class="tagline">More fun if you´ll come!</span></div>

    <section class="photo-area" role="img" aria-label="Photo of the couple">
      <span class="photo-label">PHOTO</span>
    </section>

    <footer class="date-block">
      <p class="date-headline">THE BIG DAY IS COMING</p>
      <p class="date-detail">SEPTEMBER 2012</p>
      <p class="date-detail">LOCATION</p>
    </footer>
  </main>
</body>
</html>
```